NEED BILLBOARDS FOR VELMORANCIA

we need to redo our billboards for our business. we want to have catchy, great billboards that follow standard billboard design rules. we do breast and body cosmetic surgery in Bakersfield, fresno, and stockton ca. see attached for some tips. i would like something creative, but conservative, but funny. we also won finest around 18 years in a row and can give you the logo

Target Market(s)

females 21-45

Industry/Entity Type

plastic surgery of the breast and body

Font styles to use
Serif

Requirements
Nice to have
• funny, catchy
Should not have
• pictures of women that are overly exposed

```html
<!DOCTYPE html>
<html lang="en">
<head>
<meta charset="utf-8">
<title>Velmorancia Billboard</title>
<link href="https://fonts.googleapis.com/css2?family=Tinos:wght@400;700&display=swap" rel="stylesheet">
<style>
  :root {
    --page-bg: #ffffff;
    --green-deep: #0f3f27;
    --green-mid: #1d5c3b;
    --green-light: #2a6e49;
    --text-white: #ffffff;
    --brand-tint: #dbe9c9;
    --pink-soft: #e7a9c2;
    --skin-warm: #c99a86;
    --hair-dark: #4a3428;
  }
  * { margin: 0; padding: 0; box-sizing: border-box; }
  html, body {
    width: 851px;
    height: 1200px;
    overflow: hidden;
    background: var(--page-bg);
  }
  .canvas {
    position: relative;
    width: 851px;
    height: 1200px;
  }
  .billboard {
    position: absolute;
    left: 20px;
    top: 438px;
    width: 811px;
    height: 324px;
    overflow: hidden;
    background: radial-gradient(ellipse at 35% 45%, var(--green-light) 0%, var(--green-mid) 45%, var(--green-deep) 100%);
    font-family: "Tinos", "Times New Roman", serif;
  }
  .brand {
    position: absolute;
    left: 42px;
    top: 44px;
    display: flex;
    align-items: center;
    gap: 10px;
  }
  .brand-dot {
    width: 14px;
    height: 14px;
    border-radius: 50%;
    background: var(--brand-tint);
  }
  .brand-name {
    font-size: 34px;
    font-weight: 400;
    color: var(--brand-tint);
    letter-spacing: 0.5px;
  }
  .headline {
    position: absolute;
    left: 42px;
    top: 128px;
    color: var(--text-white);
    font-weight: 700;
    text-transform: uppercase;
    line-height: 1.12;
  }
  .headline .line-one { display: block; font-size: 36px; }
  .headline .line-two { display: block; font-size: 28.5px; }
  .web-address {
    position: absolute;
    left: 42px;
    top: 230px;
    color: var(--text-white);
    font-size: 28px;
    font-weight: 700;
    letter-spacing: 0.5px;
  }
  .butterfly-accent {
    position: absolute;
    left: 418px;
    top: 84px;
    width: 40px;
    height: 34px;
    border-radius: 40%;
    background: radial-gradient(circle, var(--pink-soft) 0%, rgba(231,169,194,0.4) 100%);
  }
  .portrait {
    position: absolute;
    right: 0;
    top: 0;
    width: 340px;
    height: 324px;
    background:
      radial-gradient(ellipse at 55% 55%, var(--skin-warm) 0%, rgba(201,154,134,0.7) 38%, rgba(74,52,40,0.0) 70%),
      linear-gradient(90deg, rgba(29,92,59,0) 0%, var(--hair-dark) 30%, #6b4a38 70%, var(--hair-dark) 100%);
  }
</style>
</head>
<body>
  <main class="canvas">
    <section class="billboard">
      <div class="brand">
        <span class="brand-dot"></span>
        <span class="brand-name">Velmorancia</span>
      </div>
      <h1 class="headline">
        <span class="line-one">You do your best</span>
        <span class="line-two">when you feel your best</span>
      </h1>
      <p class="web-address">www.velmorancia.com</p>
      <div class="butterfly-accent" role="img" aria-label="Small pink butterfly illustration"></div>
      <div class="portrait" role="img" aria-label="Photograph of a woman with dark hair and soft makeup, shown from the shoulders up"></div>
    </section>
  </main>
</body>
</html>
```